Seriöses Webdesign für innovatives Ingenieurbüro mit dem Schwerpunkt Eisenbahn Leit- und Sicherungstechnik
Zielgruppe
Die Webseite hat in erster Linie die Aufgabe zu informieren: An erster Stelle steht die Kontaktaufnahme und der Kompetenzbereich des Ingenieurbüros.
Folgende Kernkompetenzen sollen durch die Webseite transportiert werden:
Hardware-Entwicklung
Software-Entwicklung
Erneuerung alter Techniken
Begutachtung
Software für Lieferantenbewertung
Störungsmanagement(system)
Zielgruppe:
Die Webseite soll als Online-Visitenkarte für bestehende und neue Kontakte dienen. Gerade neue (Messe-)Kontakte erleben die Webseite als erste Anlaufstelle und erhalten einen Einblick in das vorhandene Leistungsspektrum des Ingenieurbüros und die Möglichkeiten der Kontaktaufnahme.

```html
<!DOCTYPE html>
<html lang="de">
<head>
<meta charset="utf-8">
<title>Brenta Consult – Ingenieurbüro für Leit- und Sicherungstechnik</title>
<link href="https://fonts.googleapis.com/css2?family=Source+Sans+3:wght@400;600;700&display=swap" rel="stylesheet">
<style>
  :root{
    --sky:#7cc3e2;
    --slate:#2c3842;
    --slate-line:#3e4b56;
    --slate-soft:#3a4752;
    --white:#ffffff;
    --ink:#2b2f33;
    --page:#ffffff;
  }
  *{box-sizing:border-box;margin:0;padding:0}
  html,body{width:1113px;height:1200px;overflow:hidden;background:var(--page)}
  body{font-family:"Source Sans 3",sans-serif;color:var(--ink);position:relative}

  .site-header{position:absolute;left:0;top:0;width:1113px;height:92px;background:var(--sky)}
  .brand{position:absolute;left:165px;top:24px;font-size:34px;font-weight:700;color:var(--white);line-height:44px}
  .lang-switch{position:absolute;left:884px;top:31px;width:72px;height:38px}
  .lang-switch .map{position:absolute;inset:0;background:radial-gradient(ellipse at 60% 50%,#b9e0f1 0%,rgba(185,224,241,.2) 75%);border-radius:6px}
  .lang-switch a{position:absolute;top:6px;font-size:10px;font-weight:700;color:var(--slate);text-decoration:none;padding:2px 5px}
  .lang-switch .de{left:0;background:var(--white)}
  .lang-switch .en{left:35px}

  .hero{position:absolute;left:0;top:92px;width:1113px;height:329px;
    background:linear-gradient(180deg,#8d9cad 0%,#a7b4c2 35%,#b8bec3 58%,#7d7a70 78%,#8a8f6a 100%)}
  .service-nav{position:absolute;left:165px;top:125px;width:238px;list-style:none}
  .service-nav li{height:33px;line-height:33px;padding-left:10px;background:var(--slate);color:var(--white);
    font-size:13.6px;font-weight:600;border-bottom:1px solid var(--slate-line);white-space:nowrap}
  .service-nav li.active{background:var(--sky);color:var(--slate)}

  .intro{position:absolute;left:0;top:421px;width:1113px;height:291px;background:var(--slate);color:var(--white)}
  .intro h1{position:absolute;left:165px;top:34px;font-size:37px;font-weight:400;line-height:42px}
  .intro .route-art{position:absolute;left:371px;top:22px;width:265px;height:90px;border-radius:4px;
    background:linear-gradient(90deg,rgba(255,255,255,.04) 0%,rgba(255,255,255,.10) 100%)}
  .intro .tagline{position:absolute;left:165px;top:127px;font-size:17px;font-weight:600;color:var(--sky);line-height:22px}
  .intro .lead{position:absolute;left:165px;top:181px;width:372px;font-size:12.7px;line-height:20.3px}

  .contact{position:absolute;left:722px;top:106px;width:300px}
  .contact h2{font-size:30px;font-weight:700;color:var(--sky);line-height:34px}
  .contact .phone{font-size:13px;font-weight:700;margin-top:4px;line-height:18px}
  .contact dt{font-size:13px;font-weight:700;color:var(--sky);margin-top:12px;line-height:16px}
  .contact dd{font-size:10.5px;font-weight:700;line-height:14px}
  .contact dt.second{margin-top:5px}

  .features{position:absolute;left:0;top:712px;width:1113px;height:377px}
  .feature{position:absolute;top:60px;width:230px}
  .feature svg{position:absolute;left:0;top:0}
  .feature h3{position:absolute;top:20px;font-size:19px;font-weight:600;color:var(--ink);letter-spacing:.4px;white-space:nowrap}
  .feature p{font-size:12.7px;line-height:18.7px}
  .feature .body{position:absolute;left:0;top:70px;width:222px}
  .feature .accent{color:var(--sky)}
  .feature .accent+p{margin-top:18.7px}
  .f1{left:166px}.f1 h3{left:59px}
  .f2{left:461px}.f2 h3{left:48px}
  .f3{left:728px}.f3 h3{left:36px}

  .site-footer{position:absolute;left:0;top:1089px;width:1113px;height:111px;background:var(--sky)}
  .footer-brand{position:absolute;left:165px;top:30px;font-size:24px;font-weight:700;color:var(--white)}
  .message-btn{position:absolute;left:724px;top:40px;width:154px;height:29px;border:1px solid var(--white);
    color:var(--white);font-size:13px;font-weight:700;text-align:center;line-height:27px;text-decoration:none}
  .footer-links{position:absolute;left:165px;top:83px;font-size:11px;font-weight:600;color:var(--slate)}
  .footer-links a{color:inherit;text-decoration:none}
  .footer-links span{margin:0 4px}
</style>
</head>
<body>
<header class="site-header">
  <div class="brand">Brenta Consult</div>
  <div class="lang-switch">
    <div class="map" role="img" aria-label="Weltkarte als Hintergrund der Sprachauswahl"></div>
    <a class="de" href="#">DE</a><a class="en" href="#">ENG</a>
  </div>
</header>

<section class="hero" role="img" aria-label="Foto: zwei Hochgeschwindigkeitszüge vor einer Werkshalle auf Gleisen">
</section>
<ul class="service-nav">
  <li>Hardware-Entwicklung</li>
  <li>Software-Entwicklung</li>
  <li class="active">Erneuerung alter Techniken</li>
  <li>Begutachtung</li>
  <li>Software für Lieferantenbewertung</li>
</ul>

<section class="intro">
  <h1>Wir stellen<br>Weichen</h1>
  <div class="route-art" role="img" aria-label="Illustration: gepunkteter Weg von einem Bildschirm zu einer Weiche mit Gleisen"></div>
  <p class="tagline">Maßgeschneiderte Softwarelösungen</p>
  <p class="lead">Hier sollte ein Text stehen, der uns zum Vorteil gereift. Hier sollte ein Text stehen, der uns zum Vorteil gereift. Hier sollte ein Text stehen, der uns zum Vorteil</p>

  <div class="contact">
    <h2>Kontakt zu uns</h2>
    <p class="phone">0 800 - 12 34 56 78</p>
    <dl>
      <dt>Montag – Donnerstag</dt>
      <dd>08:00 – 12:00 Uhr / 13:30 – 17:00 Uhr</dd>
      <dt class="second">Freitag</dt>
      <dd>8:00 – 12:00 Uhr</dd>
    </dl>
  </div>
</section>

<section class="features">
  <article class="feature f1">
    <svg width="42" height="36" viewBox="0 0 42 36" fill="#2c3842">
      <rect x="1" y="1" width="38" height="20" fill="none" stroke="#2c3842" stroke-width="1.5"/>
      <circle cx="10" cy="20" r="3.5"/><circle cx="20" cy="20" r="3.5"/><circle cx="34" cy="25" r="3.5"/>
      <rect x="4" y="25" width="12" height="9" rx="3"/><rect x="17" y="25" width="8" height="9" rx="3"/><rect x="29" y="29" width="11" height="6" rx="3"/>
      <line x1="26" y1="17" x2="33" y2="6" stroke="#2c3842" stroke-width="2"/>
    </svg>
    <h3>Schulungen</h3>
    <div class="body">
      <p class="accent">Hier sollte ein Text stehen, der uns zum Vorteil gereift. Hier sollte ein Text stehen.</p>
      <p>Hier sollte ein Text stehen, der uns zum Vorteil gereift. Hier sollte ein Text stehen. Hier sollte ein Text stehen, der uns zum Vorteil gereift. Hier sollte ein Text stehen.</p>
    </div>
  </article>
  <article class="feature f2">
    <svg width="32" height="50" viewBox="0 0 32 50" fill="#2c3842">
      <circle cx="12" cy="2.5" r="2"/><circle cx="20" cy="2.5" r="2"/>
      <rect x="0" y="6" width="32" height="34" rx="8"/>
      <rect x="5" y="12" width="22" height="10" rx="2" fill="#fff"/>
      <circle cx="8" cy="31" r="2.5" fill="#fff"/><circle cx="24" cy="31" r="2.5" fill="#fff"/>
      <path d="M6 40 L1 49 H5 L9 42 H23 L27 49 H31 L26 40 Z"/>
    </svg>
    <h3>Spezialgebiete</h3>
    <div class="body">
      <p class="accent">Hier sollte ein Text stehen, der uns zum Vorteil gereift. Hier sollte ein Text stehen. Hier sollte ein Text stehen.Hier sollte ein Text stehen.</p>
      <p>Hier sollte ein Text stehen, der uns zum Vorteil gereift. Hier sollte ein</p>
    </div>
  </article>
  <article class="feature f3">
    <svg width="26" height="24" viewBox="0 0 26 24" fill="#2c3842" style="top:16px">
      <rect x="9" y="0" width="8" height="2"/><rect x="9" y="3" width="8" height="2"/>
      <path d="M9 6 H17 V11 H22 L13 19 L4 11 H9 Z"/>
      <path d="M1 14 H4 V20 H22 V14 H25 V23 H1 Z"/>
    </svg>
    <h3>Downloads</h3>
    <div class="body" style="width:230px">
      <p>Hier sollte ein Text stehen, der uns zum Vorteil gereift.</p>
    </div>
  </article>
</section>

<footer class="site-footer">
  <div class="footer-brand">Brenta</div>
  <a class="message-btn" href="#">Nachricht senden &gt;&gt;</a>
  <nav class="footer-links">
    <a href="#">Startseite</a><span>•</span><a href="#">AGB</a><span>•</span><a href="#">Bankverbindung</a><span>•</span><a href="#">Datenschutz</a><span>•</span><a href="#">Impressum</a>
  </nav>
</footer>
</body>
</html>
```